Esoteric, wellness company labels

Verdant Quillory is a lifestyle brand with multiple products. We have an offshoot as well called Marrowind Coffee. I need multiple labels or packaging designs that all match so I can start wholesaling.

I want something fun and very eye catching. I have two different logos for Verdant Quillory but just one for the coffee. I’m
Undecided which one I want on the labels because I like both. So either would work. Any coffee products go under marrowind coffee and any other products go under Verdant Quillory.

We sell items such as crystals, tarot and oracle decks, candles, organic coffee, superfood powders and herbs and more.

The items I need labels for should have a streamline look so that all are recognizable as the Verdant Quillory brand. The products that are a priority are:
Organic coffee
Reishi infused coffee
Lion’s Mane infused coffee
Those go under Marrowind Coffee.

Soon I’ll do more items;
Sacred smudging spray
Sacred smudging cleaner
Multiple superfoods
Etc
Updates

We have decided to use compostable coffee bags that are approximately 9x6x33cm so your standard 1lb bag you would see in a store. We still want colorful and eye catching but at the same time being eco friendly. The coffee is 100% organic, free trade, low acid.

We are looking for labels for the coffee but also want to be able to use the same kind of design or similar down the road for our other products. We carry superfood powders (lion’s mane, blue Spirulina, reishi, pearl powder, sea moss etc) but also things like smudging spray, rose water, neroli water, essential oils etc. we are a lifestyle company so we are looking for labels across our store brand items.

Target Market(s)

Esoteric, health and wellness, “new age”

Industry/Entity Type

Retail, wellness,

Colors

Designer to choose colors to be used in the design.

Requirements
Must have
• Beauty, attraction
Should not have
• Anything to do with religion, no dark witchy themes

```html
<!DOCTYPE html>
<html lang="en">
<head>
<meta charset="UTF-8">
<title>Marrowind Coffee – Bag Label</title>
<link rel="stylesheet" href="https://fonts.googleapis.com/css2?family=Fraunces:opsz,wght@144,600&family=Cormorant+Garamond:wght@500;600&display=swap">
<style>
  :root {
    --backdrop: #9a9a9a;
    --bag-white: #f4f1ed;
    --ink-navy: #1c2340;
    --terracotta: #c9745a;
    --sand: #e6cdb4;
    --peach: #dca184;
    --blush: #efd9c8;
    --sage: #7d8a6c;
  }
  * { margin: 0; padding: 0; box-sizing: border-box; }
  html, body {
    width: 1200px;
    height: 1199px;
    overflow: hidden;
    background: var(--backdrop);
  }
  .label {
    position: absolute;
    left: 320px;
    top: 100px;
    width: 560px;
    height: 1000px;
    background: var(--bag-white);
    overflow: hidden;
  }
  .lifestyle-photo {
    position: absolute;
    left: 0;
    right: 0;
    top: 360px;
    bottom: 0;
    background:
      radial-gradient(ellipse 38% 55% at 88% 70%, rgba(125, 138, 108, 0.75), rgba(125, 138, 108, 0) 70%),
      radial-gradient(ellipse 45% 35% at 55% 62%, rgba(220, 161, 132, 0.9), rgba(220, 161, 132, 0) 75%),
      radial-gradient(ellipse 40% 30% at 15% 60%, rgba(244, 241, 237, 0.9), rgba(244, 241, 237, 0) 75%),
      radial-gradient(ellipse 35% 25% at 18% 18%, rgba(201, 116, 90, 0.55), rgba(201, 116, 90, 0) 75%),
      linear-gradient(180deg, rgba(230, 205, 180, 0) 0%, var(--sand) 18%, var(--blush) 55%, var(--peach) 100%);
  }
  .brand-dot {
    position: absolute;
    left: 50%;
    top: 100px;
    width: 64px;
    height: 64px;
    margin-left: -32px;
    border-radius: 50%;
    background: var(--ink-navy);
  }
  .wordmark {
    position: absolute;
    left: 0;
    right: 0;
    top: 245px;
    text-align: center;
    font-family: "Fraunces", Georgia, serif;
    font-weight: 600;
    font-size: 62px;
    line-height: 0.95;
    color: var(--ink-navy);
    letter-spacing: 0.5px;
  }
  .parent-frame {
    position: absolute;
    left: 50%;
    top: 397px;
    width: 222px;
    margin-left: -111px;
    padding: 10px 0 8px;
    border: 1.5px solid var(--ink-navy);
    text-align: center;
    font-family: "Cormorant Garamond", Georgia, serif;
    font-weight: 600;
    font-size: 19px;
    line-height: 1.15;
    letter-spacing: 5px;
    color: var(--ink-navy);
  }
  .web-address {
    position: absolute;
    left: 0;
    right: 0;
    top: 502px;
    text-align: center;
    font-family: "Cormorant Garamond", Georgia, serif;
    font-weight: 500;
    font-size: 12px;
    letter-spacing: 3px;
    text-transform: uppercase;
    color: var(--ink-navy);
  }
</style>
</head>
<body>
  <main class="label">
    <div class="lifestyle-photo" role="img" aria-label="Lifestyle photo of embroidered cream and terracotta cushions with green leaves"></div>
    <div class="brand-dot"></div>
    <h1 class="wordmark">MARROWIND<br>COFFEE</h1>
    <div class="parent-frame">VERDANT<br>QUILLORY</div>
    <p class="web-address">verdantquillory.com</p>
  </main>
</body>
</html>
```